IT Company that provides secure IT solutions and services to our customers

We need business cards and a logo for a new IT Solutions company just created based in Kuala Lumpur, Malaysia. But will also be serving other countries in the region. We provide secure data, voice solutions on mobile platforms. Our first offering is encrypted voice and data solutions for IOS, Android, Windows and BlackBerry devices.

Target Market(s)

large organizations Govt, Police, Defence, Anti-corruption, Legal, highly regulated industries such as Health-care, Financial, Banking, Insurance,

Industry/Entity Type

Information Technology

Contact Information for Business Card

VornaxIT (Logo - colour is ORBEL blue)Dariush Pelo Managing Director Vornax IT Sdn. Bhd.5th Floor, Block F, Wisma LBD,No.14 Jalan Seri Mewah,50470, Kuala LumpurMalaysia

Font styles to use
Sans Serif

Colors
3176b5
ec1f27
fbed22

Requirements
Must have
• VornaxIT all in Blue like ORBEL blue. A logo design perhaps a play of VI, K with a dangling T (colour can be any)
Nice to have
• I want a clean crisp card, not too busy, easy to read.

```html
<!DOCTYPE html>
<html lang="en">
<head>
<meta charset="utf-8">
<title>Vornax IT Business Card</title>
<link rel="stylesheet" href="https://fonts.googleapis.com/css2?family=Arimo:wght@400&display=swap">
<style>
  :root {
    --canvas: #ffffff;
    --card-yellow: #f8df12;
    --accent-orange: #f2a91f;
    --brand-red: #e2231f;
    --brand-blue: #3176b5;
    --ink: #111111;
    --shadow: #c4c4c4;
  }
  * { margin: 0; padding: 0; box-sizing: border-box; }
  html, body {
    width: 1200px;
    height: 838px;
    overflow: hidden;
    background: var(--canvas);
    font-family: "Arimo", Arial, sans-serif;
  }
  .canvas { position: relative; width: 1200px; height: 838px; }

  .card {
    position: absolute;
    width: 460px;
    height: 264px;
    background: var(--card-yellow);
    overflow: hidden;
  }
  .card--front {
    left: 333px;
    top: 156px;
    box-shadow: 7px 7px 0 var(--shadow);
  }
  .card--back {
    left: 338px;
    top: 457px;
  }

  .front__accent {
    position: absolute;
    left: 152px;
    top: 26px;
    width: 200px;
    height: 200px;
    background: var(--accent-orange);
    opacity: 0.55;
  }
  .front__text {
    position: absolute;
    left: 68px;
    top: 70px;
    width: 321px;
    color: var(--ink);
  }
  .front__name {
    font-size: 30px;
    font-weight: 400;
    letter-spacing: 9.2px;
    line-height: 34px;
    white-space: nowrap;
  }
  .front__details {
    margin-top: 6px;
    font-size: 15.5px;
    line-height: 24.5px;
    text-align: justify;
    text-align-last: justify;
  }

  .back__mark {
    position: absolute;
    left: 211px;
    top: 46px;
    width: 38px;
    height: 38px;
    background: var(--brand-red);
  }
  .back__name {
    position: absolute;
    left: 0;
    right: 0;
    top: 145px;
    text-align: center;
    font-size: 41px;
    font-weight: 400;
    line-height: 48px;
    color: var(--brand-blue);
  }
</style>
</head>
<body>
<main class="canvas">
  <section class="card card--front" aria-label="Business card front">
    <div class="front__accent" aria-hidden="true"></div>
    <div class="front__text">
      <h1 class="front__name">Dariush Pelo</h1>
      <p class="front__details">Managing Director Vornax IT Sdn. Bhd.5th Floor, Block F, Wisma LBD,No.14 Jalan Seri Mewah,50470, Kuala Lumpur Malaysia</p>
    </div>
  </section>

  <section class="card card--back" aria-label="Business card back">
    <div class="back__mark" aria-hidden="true"></div>
    <p class="back__name">VornaxIT</p>
  </section>
</main>
</body>
</html>
```